Twin Ravens Sparkling

Hi all,

Thanks for taking the time to check out our brief.

Twin Ravens is an Australian wine company based in Victoria, and have been around for more than 20 years. We have a well-known sparkling Chardonnay Pinot Noir that needs a package revamp and we need your help!

Check out our current package here: http://www.twinravens.example.au/our-wines/dsp-default_b.cfm?loadref=17

So here's the brief:

1. Use of the Twin Ravens logo (silhouette) and text mandatory - but can be as small/large as required.

2. Design must be shown on a sparkling bottle.

3. Can be closed with cork or crown seal - neck label/hood not mandatory.

4. Front label size to be no larger than 75mm high x 100mm wide. Back label to be no larger than 75mm x 100mm

5. Label does not have to be square/rectangular. Happy to see thoughts outside the box.

6. Design cannot be printed onto the bottle - must be on a label that can be applied to the bottle.

7. Be forward thinking. Be interesting. This design does not have to tie into our still (red and white) wine range.

8. Mandatory information to be shown on front label - a. Wine of Australia - b. Sparkling Chardonnay Pinot Noir

9. Mandatory info for front label - a. 750mL - b. Alcohol e.g. 13.5% ALC/VOL - c. Wine of Australi - d. Producer address (please insert dummy address at this stage - e. standard drinks e.g. approx 8.0 standard drinks (this can also be shown in the standard drinks glass logo) - f. space for a tasting blurb

10. Try to stay away from anything floral or overly girly.

Requirements
Must have
• Design must be shown on a sparkling wine bottle & include the full label design separately
Should not have
• Try to stay away from anything too floral and overly girly.

```html
<!DOCTYPE html>
<html lang="en">
<head>
<meta charset="utf-8">
<title>Twin Ravens Sparkling – Label Design</title>
<link rel="stylesheet" href="https://fonts.googleapis.com/css2?family=Cormorant+Garamond:ital,wght@0,500;1,400&family=Arimo:wght@400&display=swap">
<style>
  :root {
    --bg-centre: #ffffff;
    --bg-edge: #d9dadc;
    --pearl-light: #fbf9f3;
    --pearl-mid: #e6e2d8;
    --pearl-dark: #cfc9bb;
    --gold-light: #f3d7a6;
    --gold-mid: #d2a160;
    --gold-dark: #a8743a;
    --wine-red: #5a2418;
    --ink: #2b2420;
    --ink-soft: #4a4440;
    --muted: #8b857c;
    --silhouette: #2f2c2a;
  }
  * { margin: 0; padding: 0; box-sizing: border-box; }
  html, body { width: 1200px; height: 1000px; overflow: hidden; }
  body {
    position: relative;
    background: radial-gradient(ellipse at 50% 45%, var(--bg-centre) 35%, var(--bg-edge) 100%);
    font-family: "Arimo", Arial, sans-serif;
    color: var(--ink);
  }
  .front-label-shape { position: absolute; left: 0; top: 0; }
  .brand-name {
    font-family: "Cormorant Garamond", Georgia, serif;
    font-weight: 500;
    color: var(--ink);
    text-transform: uppercase;
    white-space: nowrap;
  }
  .origin {
    font-family: "Cormorant Garamond", Georgia, serif;
    font-style: italic;
    color: var(--muted);
    white-space: nowrap;
  }
  .abs { position: absolute; }

  /* Front label */
  .front-label .brand-name { left: 412px; width: 400px; top: 174px; text-align: center; font-size: 28px; letter-spacing: 0.26em; }
  .front-label .style { left: 412px; width: 400px; top: 232px; text-align: center; font-size: 14px; color: var(--wine-red); }
  .front-label .variety { left: 412px; width: 400px; top: 252px; text-align: center; font-size: 22px; color: var(--wine-red); }
  .front-label .origin { left: 412px; width: 400px; top: 302px; text-align: center; font-size: 11px; }
  .front-label .emblem {
    left: 590px; top: 330px; width: 46px; height: 54px;
    background: linear-gradient(180deg, rgba(120,110,100,0.22), rgba(120,110,100,0.10));
    border-radius: 4px;
  }

  /* Back label */
  .back-label {
    left: 428px; top: 530px; width: 370px; height: 283px;
    background: linear-gradient(100deg, var(--pearl-mid) 0%, var(--pearl-light) 40%, var(--pearl-light) 60%, var(--pearl-dark) 100%);
  }
  .back-label .brand-name { left: 16px; top: 14px; font-size: 31px; letter-spacing: 0.33em; }
  .back-label .silhouette-art {
    left: 12px; top: 64px; width: 96px; height: 146px;
    background: linear-gradient(180deg, #3a3633, var(--silhouette));
    border-radius: 40px 40px 6px 6px;
  }
  .back-label .style { left: 120px; top: 65px; font-size: 13px; color: var(--ink-soft); }
  .back-label .variety { left: 118px; top: 80px; font-size: 27px; line-height: 27px; color: var(--ink); }
  .back-label .origin { left: 120px; top: 137px; font-size: 12px; }
  .back-label .blurb {
    left: 120px; top: 154px; width: 240px;
    font-family: "Cormorant Garamond", Georgia, serif; font-style: italic;
    font-size: 14px; line-height: 14px; letter-spacing: 0.02em; color: var(--ink-soft);
  }
  .back-label .address { left: 29px; top: 224px; font-size: 12px; line-height: 13.5px; color: var(--ink-soft); }
  .back-label .drinks-badge {
    left: 180px; top: 230px; width: 32px; height: 44px;
    background: var(--ink); border-radius: 3px;
  }
  .back-label .volume { left: 276px; top: 226px; width: 70px; text-align: center; font-size: 14.5px; line-height: 17px; color: var(--ink-soft); }
</style>
</head>
<body>

<svg class="front-label-shape" width="1200" height="1000" viewBox="0 0 1200 1000" aria-hidden="true">
  <defs>
    <linearGradient id="pearl" x1="0" y1="0" x2="1" y2="1">
      <stop offset="0" stop-color="#e9e5dc"/>
      <stop offset="0.45" stop-color="#fbf9f3"/>
      <stop offset="1" stop-color="#d8d2c4"/>
    </linearGradient>
    <linearGradient id="gold-band" x1="0" y1="0" x2="1" y2="0">
      <stop offset="0" stop-color="#d2a160"/>
      <stop offset="0.5" stop-color="#f3d7a6"/>
      <stop offset="1" stop-color="#d2a160"/>
    </linearGradient>
    <clipPath id="oval-clip">
      <ellipse cx="612" cy="252" rx="190" ry="150"/>
    </clipPath>
  </defs>
  <ellipse cx="612" cy="252" rx="190" ry="150" fill="url(#pearl)" stroke="#c9a06a" stroke-width="2"/>
  <rect x="400" y="226" width="424" height="64" fill="url(#gold-band)" clip-path="url(#oval-clip)"/>
</svg>

<section class="front-label">
  <div class="abs brand-name">Twin Ravens</div>
  <div class="abs style">SPARKLING</div>
  <div class="abs variety">CHARDONNAY PINOT NOIR</div>
  <div class="abs origin">Wine of Australia</div>
  <div class="abs emblem" role="img" aria-label="Faint brand silhouette emblem"></div>
</section>

<section class="abs back-label">
  <div class="abs brand-name">Twin Ravens</div>
  <div class="abs silhouette-art" role="img" aria-label="Brand silhouette illustration"></div>
  <div class="abs style">SPARKLING</div>
  <div class="abs variety">CHARDONNAY<br>PINOT NOIR</div>
  <div class="abs origin">Wine of Australia</div>
  <p class="abs blurb">Enjoy a premium non-vintage wine made from selected Chardonnay and Pinot Noir grapes, displaying classic citrus flavours with a delicate crisp finish.</p>
  <div class="abs address">PO Box 1000<br>Kelby Vale<br>VIC 3999<br>Australia</div>
  <div class="abs drinks-badge" role="img" aria-label="Standard drinks badge"></div>
  <div class="abs volume">750mL<br>13.5%<br>ALC/VOL</div>
</section>

</body>
</html>
```